Small corporate website template design

I need a couple templates designed for a small corporate website. The corporate site reflects the existence of the parent company which will own various brands/services that have their own websites, so it will mainly be used to present who we are, what we do, what is happening (news/events), how to contact us, link off to our other brand/service sites, as well as post information for public relations, investors, and job opportunities.

The company name is Vornelight LLC (www.vornelight.example), and the name is representative of stratified layers of interconnected digital services. The corporate site is not expected to generate a bunch of fanfare - that honor will be reserved for the externally linked brand/service sites.

The provided logo may be manipulated in color, size, shape, positioning, etc. to get it to fit with the design, but should be integrated in some way.

What we are looking for is a home page layout as well as a template for an inner page whereby the navigation/logo, etc may be diminished to some extent for the inner pages. We are also interested in reusable elements such as dividers, content containers, etc. in order to represent the types of information described above that we would like to present as described above.

We are particularly interested in consistency of design elements, conservative use of color (including consideration of accessibility concerns), judicious use of whitespace in favor of simplified messaging, and something lending itself well to internationalization/translation.

Target Market(s)

Small business owners, entrepreneurs (B2B)

Number of Pages Required

2 page

Font styles to use
Sans Serif

Requirements
Must have
• See the attached PDF with the logo concept, color swatches, and comparative sites.

```html
<!DOCTYPE html>
<html lang="en">
<head>
<meta charset="utf-8">
<title>Vornelight LLC</title>
<link rel="stylesheet" href="https://fonts.googleapis.com/css2?family=Open+Sans:ital,wght@0,300;0,400;0,600;1,300;1,400&family=Prompt:wght@400;500&display=swap">
<style>
  :root {
    --navy: #0b1f7a;
    --ink: #111111;
    --grey: #555555;
    --white: #ffffff;
    --band-deep: #030a26;
    --band-blue: #0a2a9e;
    --hero-blue: #0a3cf0;
    --hero-deep: #02127a;
    --rule: #0b1250;
    --social-a: #1c9be0;
    --social-b: #2d4a8f;
    --social-c: #c4101a;
    --social-d: #0a6aa6;
  }
  * { box-sizing: border-box; margin: 0; padding: 0; }
  html, body { width: 992px; height: 1200px; overflow: hidden; background: var(--white); }
  body { position: relative; font-family: "Open Sans", Arial, sans-serif; color: var(--ink); }

  .hero { position: absolute; left: 0; top: 0; width: 992px; height: 160px;
    background: radial-gradient(ellipse at 70% 20%, var(--hero-blue) 0%, #0726b8 45%, var(--hero-deep) 100%); }
  .hero-curve { position: absolute; left: 0; top: 0; width: 992px; height: 160px; }
  .brand { position: absolute; left: 139px; top: 18px; display: flex; align-items: center; gap: 8px;
    font-family: "Prompt", sans-serif; font-weight: 500; font-size: 20px; color: var(--white); }
  .brand-mark { width: 14px; height: 14px; background: var(--white); }
  .main-nav { position: absolute; top: 19px; left: 0; width: 992px; }
  .main-nav a { position: absolute; font-family: "Prompt", sans-serif; font-size: 16px; color: var(--white); text-decoration: none; }

  .section-title { position: absolute; left: 0; width: 992px; text-align: center;
    font-family: "Prompt", sans-serif; font-weight: 400; font-size: 22px; color: var(--grey); letter-spacing: .3px; }
  .section-title span { color: var(--navy); }
  .lead { position: absolute; left: 184px; width: 624px; text-align: center;
    font-weight: 300; font-size: 13.9px; line-height: 21.3px; color: var(--grey); }

  .about-icon { position: absolute; left: 477px; top: 187px; width: 38px; height: 38px; border-radius: 50%; background: var(--navy); }

  .who { position: absolute; left: 0; top: 350px; width: 992px; height: 379px; display: flex; }
  .who-left { width: 514px; height: 100%; background: linear-gradient(90deg, var(--band-deep) 0%, #06185e 60%, var(--band-blue) 100%); position: relative; }
  .who-right { flex: 1; height: 100%; background: linear-gradient(90deg, var(--band-deep) 0%, #061b70 55%, var(--band-blue) 100%); position: relative; }
  .who h2 { position: absolute; left: 126px; top: 24px; font-family: "Prompt", sans-serif; font-weight: 400; font-size: 22px; color: var(--white); }
  .who p { position: absolute; left: 126px; top: 74px; width: 362px; font-size: 13.6px; line-height: 21.2px; color: var(--white); }
  .feature { position: absolute; left: 28px; width: 398px; height: 79px; border: 1px solid rgba(255,255,255,.85);
    display: flex; align-items: center; padding-left: 16px; gap: 20px; color: var(--white); font-size: 16px; }
  .feature svg { width: 46px; height: 46px; flex: none; }

  .footer { position: absolute; left: 0; top: 957px; width: 992px; height: 243px; border-top: 1.5px solid var(--rule); }
  .footer .brand { position: absolute; left: 139px; top: 16px; color: var(--ink); font-size: 20px; }
  .footer .brand-mark { background: var(--ink); }
  .contact { position: absolute; left: 140px; top: 72px; font-style: italic; font-size: 12.5px; color: var(--ink); }
  .contact h4 { font-weight: 400; font-size: 13px; margin-bottom: 16px; }
  .contact address { font-style: italic; font-weight: 300; line-height: 16px; }
  .contact .phone { margin-top: 14px; }
  .link-col { position: absolute; top: 45px; }
  .link-col h4 { font-weight: 400; font-size: 13px; margin-bottom: 12px; height: 16px; }
  .link-col ul { list-style: none; }
  .link-col li { font-size: 11.5px; line-height: 21px; }
  .social { position: absolute; left: 788px; top: 50px; }
  .social h4 { font-weight: 400; font-size: 13px; margin-bottom: 12px; }
  .social-row { display: flex; gap: 9px; margin-left: 2px; }
  .social-row span { width: 25px; height: 25px; display: block; }
</style>
</head>
<body>

<header class="hero" role="img" aria-label="Blue abstract background of connected network lines">
  <svg class="hero-curve" viewBox="0 0 992 160" preserveAspectRatio="none" aria-hidden="true">
    <path d="M0 158 Q496 0 992 158 L992 160 L0 160 Z" fill="#ffffff"/>
  </svg>
</header>
<div class="brand"><i class="brand-mark"></i>Vornelight LLC</div>
<nav class="main-nav">
  <a href="#" style="left:477px">About</a>
  <a href="#" style="left:554px">Our Services</a>
  <a href="#" style="left:681px">News</a>
  <a href="#" style="left:755px">Contact Us</a>
</nav>

<h1 class="section-title" style="top:130px">ABOUT <span>VORNELIGHT LLC</span></h1>
<div class="about-icon">
  <svg viewBox="0 0 38 38" width="38" height="38" aria-hidden="true" fill="none" stroke="#fff" stroke-width="1.3">
    <rect x="13" y="13" width="12" height="12" rx="1"/>
    <rect x="16.5" y="16.5" width="5" height="5"/>
    <path d="M16 10v3M19 10v3M22 10v3M16 25v3M19 25v3M22 25v3M10 16h3M10 19h3M10 22h3M25 16h3M25 19h3M25 22h3"/>
  </svg>
</div>
<p class="lead" style="top:241px">Lorem ipsum dolor sit amet, consectetur adipiscing elit. In in nisl et nisl malesuada vestibulum vel sit amet tellus. Etiam ac nulla quis felis faucibus porta sit amet non ex. Nunc ullamcorper lorem in sagittis vestibulum. In est elit, pulvinar sed maximus at, gravida ut erat. Donec vel lectus ut leo suscipit iaculis.</p>

<section class="who">
  <div class="who-left">
    <h2>WHO WE ARE?</h2>
    <p>Lorem ipsum dolor sit amet, consectetur adipiscing elit. In in nisl et nisl malesuada vestibulum vel sit amet tellus. Etiam ac nulla quis felis faucibus porta sit amet non ex. Nunc ullamcorper lorem in sagittis vestibulum. In est elit, pulvinar sed maximus at, gravida ut erat. Donec vel lectus ut leo suscipit iaculis. Proin et convallis lorem. Integer eget nibh molestie, luctus orci vitae, fringilla nibh. Vivamus laoreet imperdiet sem, sit amet facilisis augue tristique in. Cras imperdiet scelerisque quam quis rhoncus. Duis dictum, ante eu elementum ultricies, dui libero aliquet lorem, et vulputate nulla tellus at nulla. Morbi eleifend tincidunt velit sit amet commodo. Nullam a turpis et erat gravida rutrum.</p>
  </div>
  <div class="who-right">
    <div class="feature" style="top:45px">
      <svg viewBox="0 0 46 46" fill="none" stroke="#fff" stroke-width="2" aria-hidden="true">
        <path d="M6 3h26l8 8v32H6z"/><path d="M32 3v8h8"/>
        <circle cx="15" cy="15" r="3"/><circle cx="30" cy="26" r="3"/><circle cx="15" cy="34" r="3"/>
        <path d="M18 15h6q6 0 6 6v2M27 26h-6q-6 0-6 5"/>
      </svg>
      <span>Lorem ipsum dolor sit amet, consectetur</span>
    </div>
    <div class="feature" style="top:154px">
      <svg viewBox="0 0 46 46" fill="none" stroke="#fff" stroke-width="2" aria-hidden="true">
        <rect x="7" y="3" width="32" height="24" rx="2"/><path d="M13 10h20M13 15h20M13 20h20"/>
        <path d="M23 27v10M3 37h40"/><circle cx="8" cy="37" r="3"/><circle cx="23" cy="37" r="3"/><circle cx="38" cy="37" r="3"/>
      </svg>
      <span>Lorem ipsum dolor sit amet, consectetur</span>
    </div>
    <div class="feature" style="top:260px">
      <svg viewBox="0 0 46 46" fill="none" stroke="#fff" stroke-width="2.4" aria-hidden="true">
        <path d="M14 3h22v40H8V9z"/><path d="M19 8v8M24 8v8M29 8v8"/>
      </svg>
      <span>Lorem ipsum dolor sit amet, consectetur</span>
    </div>
  </div>
</section>

<h2 class="section-title" style="top:770px">JOIN <span>THE TEAM</span></h2>
<p class="lead" style="top:819px">Lorem ipsum dolor sit amet, consectetur adipiscing elit. In in nisl et nisl malesuada vestibulum vel sit amet tellus. Etiam ac nulla quis felis faucibus porta sit amet non ex. Nunc ullamcorper lorem in sagittis vestibulum. In est elit, pulvinar sed maximus at, gravida ut erat. Donec vel lectus ut leo suscipit iaculis.</p>

<footer class="footer">
  <div class="brand"><i class="brand-mark"></i>Vornelight LLC</div>
  <div class="contact">
    <h4>CONTACT</h4>
    <address>Vornelight LLC<br>Address1<br>Address2</address>
    <p class="phone">0800 555 019</p>
  </div>
  <div class="link-col" style="left:314px">
    <h4>PRODUCTS</h4>
    <ul><li>Invoices</li><li>Ledger</li><li>Transfers</li><li>Insights</li><li>Reports</li><li>Alerts</li></ul>
  </div>
  <div class="link-col" style="left:391px">
    <h4></h4>
    <ul><li>Plans</li><li>Regions</li><li>Tutorials</li></ul>
  </div>
  <div class="link-col" style="left:522px">
    <h4>COMPANY</h4>
    <ul><li>About</li><li>Customers</li><li>Jobs</li><li>Blog</li><li>Environment</li></ul>
  </div>
  <div class="link-col" style="left:654px">
    <h4>RESOURCES</h4>
    <ul><li>Support</li><li>Contact</li><li>Privacy &amp; terms</li><li>Sitemap</li></ul>
  </div>
  <div class="social">
    <h4>CONNECT WITH US</h4>
    <div class="social-row">
      <span style="background:var(--social-a)"></span>
      <span style="background:var(--social-b)"></span>
      <span style="background:var(--social-c)"></span>
      <span style="background:var(--social-d)"></span>
    </div>
  </div>
</footer>

</body>
</html>
```